Local Service Business Needing Clear Business Card Design

We are needing a business card design to be made for our power washing company. Business cards will be printed on plastic standard sized cards. We're looking for someone who can make a unique and unforgettable design. Double sided and or single sided concepts would be ideal. Of course keeping in mind we are seeking translucent cards but not married to the idea of having them as the main concern is just to have plastic cards to prevent water damage! :D

More info on our company can be found on lakeshorebrightwash.example

Not looking for a list of our services. Simply applying company info and possibly "Commercial Residential Fleet" on them tastefully and appropriate to design is all thats needed.

Phone number for our company is 855-GLO-TEAM or 855-456-8326

Industry/Entity Type

Power Washing

Contact Information for Business Card

Phone, Web URL,

Requirements
Should not have
• Bubbles, water or super distracting graphics. Looking for a simple and clean look. Unfortunately our logo is this way which we may seek to change in the near future.

```html
<!DOCTYPE html>
<html lang="en">
<head>
<meta charset="utf-8">
<title>Lakeshore Brightwash – Business Card</title>
<link rel="stylesheet" href="https://fonts.googleapis.com/css2?family=Arimo:wght@400;700&display=swap">
<style>
  :root {
    --backdrop: #a3b1be;
    --card-light: #dbe4ec;
    --card-mid: #b4c4d2;
    --ink-dark: #000000;
    --blue-deep: #0a5fc4;
    --blue-bright: #0a8fd8;
    --blue-soft: #4aaee6;
    --name-blue: #1b93d1;
    --title-ink: #151515;
    --contact-ink: #dfe6ee;
    --brand-ink: #0b2a55;
  }
  html, body {
    margin: 0;
    padding: 0;
    width: 1200px;
    height: 927px;
    overflow: hidden;
    background: var(--backdrop);
    font-family: "Arimo", Arial, sans-serif;
  }
  .card {
    position: absolute;
    left: 80px;
    top: 166px;
    width: 1040px;
    height: 596px;
    border-radius: 30px;
    overflow: hidden;
    background: radial-gradient(ellipse at 30% 35%, var(--card-light) 0%, var(--card-mid) 75%);
  }
  .card-layer {
    position: absolute;
    inset: 0;
    width: 100%;
    height: 100%;
  }
  .holder {
    position: absolute;
    left: 60px;
    top: 44px;
  }
  .holder-name {
    margin: 0;
    font-size: 35px;
    font-weight: 700;
    color: var(--name-blue);
    line-height: 1.1;
  }
  .holder-title {
    margin: 0;
    font-size: 26px;
    font-weight: 400;
    color: var(--title-ink);
    line-height: 1.2;
  }
  .brand {
    position: absolute;
    left: 545px;
    top: 82px;
    display: flex;
    align-items: center;
    gap: 16px;
  }
  .brand-dot {
    width: 34px;
    height: 34px;
    border-radius: 50%;
    background: var(--blue-deep);
    flex: none;
  }
  .brand-name {
    font-size: 46px;
    font-weight: 700;
    color: var(--brand-ink);
    line-height: 1.02;
  }
  .contact {
    position: absolute;
    left: 60px;
    top: 396px;
    margin: 0;
    padding: 0;
    list-style: none;
    color: var(--contact-ink);
    font-size: 28px;
  }
  .contact li {
    display: flex;
    align-items: center;
    gap: 14px;
    height: 34px;
  }
  .contact svg {
    width: 24px;
    height: 24px;
    flex: none;
  }
  .address {
    position: absolute;
    left: 60px;
    top: 520px;
    margin: 0;
    font-size: 27px;
    color: var(--contact-ink);
  }
</style>
</head>
<body>
  <div class="card">
    <svg class="card-layer splash-area" viewBox="0 0 1475 845" preserveAspectRatio="none" role="img" aria-label="Blue water splash illustration sweeping across the card">
      <defs>
        <linearGradient id="splashTone" x1="0" x2="1" y1="0" y2="0.4">
          <stop offset="0" stop-color="var(--blue-soft)"/>
          <stop offset="0.55" stop-color="var(--blue-deep)"/>
          <stop offset="1" stop-color="var(--blue-bright)"/>
        </linearGradient>
      </defs>
      <path d="M0 335 L40 360 C120 300 260 380 360 420 C560 470 900 420 1080 470 C1200 420 1440 420 1450 250 C1455 150 1410 60 1360 0 H1475 V845 H0 Z" fill="url(#splashTone)"/>
    </svg>
    <svg class="card-layer dark-panel" viewBox="0 0 1475 845" preserveAspectRatio="none" aria-hidden="true">
      <path d="M0 335 C60 440 150 500 260 525 C420 555 560 490 700 480 C860 470 960 560 990 650 C1010 720 960 800 900 845 H0 Z" fill="var(--ink-dark)"/>
    </svg>

    <div class="holder">
      <h1 class="holder-name">Daniel Mercer</h1>
      <p class="holder-title">Manager</p>
    </div>

    <div class="brand">
      <span class="brand-dot"></span>
      <span class="brand-name">Lakeshore<br>Brightwash</span>
    </div>

    <ul class="contact">
      <li>
        <svg viewBox="0 0 24 24" aria-hidden="true"><path fill="currentColor" d="M6.6 10.8a15.1 15.1 0 0 0 6.6 6.6l2.2-2.2c.3-.3.7-.4 1-.2 1.1.4 2.3.6 3.6.6.6 0 1 .4 1 1V20c0 .6-.4 1-1 1A17 17 0 0 1 3 4c0-.6.4-1 1-1h3.5c.6 0 1 .4 1 1 0 1.3.2 2.5.6 3.6.1.3 0 .7-.2 1z"/></svg>
        <span>855-GLO-TEAM</span>
      </li>
      <li>
        <svg viewBox="0 0 24 24" aria-hidden="true"><path fill="currentColor" d="M2 5h20v14H2z"/><path fill="none" stroke="#000" stroke-width="1.6" d="M2.5 5.5 12 13l9.5-7.5M2.5 18.5l7-6.5M21.5 18.5l-7-6.5"/></svg>
        <span>info@lakeshorebrightwash.example</span>
      </li>
      <li>
        <svg viewBox="0 0 24 24" aria-hidden="true"><circle cx="12" cy="12" r="9.5" fill="none" stroke="currentColor" stroke-width="2"/><path fill="none" stroke="currentColor" stroke-width="1.6" d="M2.5 12h19M12 2.5c3 3 3 16 0 19M12 2.5c-3 3-3 16 0 19"/></svg>
        <span>lakeshorebrightwash.example</span>
      </li>
    </ul>

    <p class="address">240 Harbor Ln., Dunmore, MI 49000</p>
  </div>
</body>
</html>
```